CTWI application splash screen

We need a 1024x768 image for use as an application splash screen.
The image will be displayed full screen on an 10 inch industrial PC 1024x768 screen while our application is launching. The image should convey that the application is "Waiting for connection to Wi-Fi access point..." and include a graphic of the industrial PC connected to the access point via an Ethernet cable. A list of troubleshooting steps should be included at the bottom of the image. The troubleshooting steps should not be the main focus of the image and should be shown in a smaller font (but still readable at 1024x768 displayed on a 10 inch screen).
I will include a mock up of the general idea of what we are looking for as well as image files for the industrial PC, a screenshot of our application to show on the PC's screen and the AP.
For general look and feel and a sense of corporate branding please review our website https://corvanetillageworks.com/. The splash screen should reflect corporate branding.
Target Market(s)
Users of our application
Industry/Entity Type
Agriculture

```html
<!DOCTYPE html>
<html lang="en">
<head>
<meta charset="utf-8">
<title>CTWI splash screen – Waiting for Wi-Fi access point</title>
<link href="https://fonts.googleapis.com/css2?family=Poppins:wght@400;500;600;700&display=swap" rel="stylesheet">
<style>
  :root {
    --stage: #000000;
    --brand-green: #43be6c;
    --text-green: #3bb865;
    --white: #ffffff;
    --device-dark: #2a2a2a;
    --device-screen: #e9ecea;
    --ap-white: #f2f2f2;
    --ap-shade: #d9dcda;
  }
  * { margin: 0; padding: 0; box-sizing: border-box; }
  html, body {
    width: 1200px; height: 1200px; overflow: hidden;
    background: var(--stage);
    font-family: "Poppins", sans-serif;
  }
  .stage { position: relative; width: 1200px; height: 1200px; }
  .splash {
    position: absolute; left: 111px; top: 233px;
    width: 978px; height: 734px;
    background: var(--brand-green);
    overflow: hidden;
  }
  .title-card {
    position: absolute; left: 283px; top: 0;
    width: 413px; height: 163px;
    background: var(--white);
    border-radius: 0 0 26px 26px;
    display: flex; align-items: center; justify-content: center;
    padding-top: 6px;
  }
  .title-card h1 {
    color: var(--text-green);
    font-weight: 700; font-size: 34px; line-height: 34px;
    letter-spacing: 1.6px; text-align: center;
  }
  .device-pc {
    position: absolute; left: 94px; top: 222px;
    width: 193px; height: 154px;
    border-radius: 10px;
    background: linear-gradient(180deg, #3a3a3a, var(--device-dark));
    border: 2px solid var(--white);
  }
  .device-pc::after {
    content: ""; position: absolute; left: 17px; top: 13px; right: 17px; bottom: 22px;
    background: linear-gradient(180deg, var(--device-screen), #cfe9d8);
    border-radius: 2px;
  }
  .device-ap {
    position: absolute; left: 753px; top: 220px;
    width: 24px; height: 158px;
    border-radius: 6px;
    background: linear-gradient(90deg, var(--ap-shade), var(--ap-white) 45%, var(--ap-shade));
  }
  .device-label {
    position: absolute; width: 300px; text-align: center;
    color: var(--white); letter-spacing: 1px;
  }
  .device-label .name { display: block; font-weight: 700; font-size: 18px; line-height: 22px; }
  .device-label .model { display: block; font-weight: 400; font-size: 16px; line-height: 22px; margin-top: 2px; }
  .label-pc { left: 41px; top: 398px; }
  .label-ap { left: 612px; top: 398px; }
  .link-line { position: absolute; left: 0; top: 0; }
  .link-caption {
    position: absolute; left: 389px; top: 463px; width: 200px;
    text-align: center; color: var(--white);
    font-weight: 600; font-size: 17px; letter-spacing: 1.2px;
  }
  .help-card {
    position: absolute; left: 276px; top: 580px;
    width: 426px; height: 160px;
    background: var(--white);
    border-radius: 26px 26px 0 0;
    padding: 10px 26px 0 28px;
    color: var(--text-green);
  }
  .help-card h2 {
    text-align: center; font-weight: 600; font-size: 14px;
    letter-spacing: 1px; line-height: 20px; margin-bottom: 2px;
  }
  .help-card ul { list-style: none; font-size: 9.6px; line-height: 11.5px; }
  .help-card li { position: relative; padding-left: 7px; }
  .help-card li::before { content: "•"; position: absolute; left: 0; }
  .help-card ul ul { padding-left: 12px; }
  .brand-mark {
    position: absolute; left: 855px; top: 630px; width: 90px;
    display: flex; align-items: center; gap: 6px;
    color: var(--white); font-weight: 700; font-size: 26px; letter-spacing: 1px;
  }
  .brand-mark .square { width: 12px; height: 12px; background: var(--white); }
</style>
</head>
<body>
<div class="stage">
  <main class="splash">
    <header class="title-card">
      <h1>Waiting for<br>connection to Wi-Fi<br>access point...</h1>
    </header>

    <div class="device-pc" role="img" aria-label="Industrial tractor cab computer showing the CTWI application screen"></div>
    <div class="device-ap" role="img" aria-label="Outdoor Wi-Fi access point with two antennas"></div>

    <div class="device-label label-pc">
      <span class="name">TRACTOR CAB</span>
      <span class="model">COMPUTER</span>
    </div>
    <div class="device-label label-ap">
      <span class="name">WI-FI ACCESS POINT</span>
      <span class="model">NETVALE AX-200 OUTDOOR</span>
    </div>

    <svg class="link-line" width="978" height="734" viewBox="0 0 978 734" aria-hidden="true">
      <path d="M191 458 V494 H762 V458" fill="none" stroke="#ffffff" stroke-width="2.6"
            stroke-linecap="round" stroke-dasharray="0 9.6"/>
    </svg>
    <div class="link-caption">ETHERNET CABLE</div>

    <section class="help-card">
      <h2>TROUBLESHOOTING STEPS:</h2>
      <ul>
        <li>This screen should only be visible for a short time on boot.</li>
        <li>If this screen stays visible for more than a minute:
          <ul>
            <li>Verify that the Wi-Fi Access Point (AP) powers up when this system does (indicated by a green light on the side of the AP).</li>
            <li>Check the Ethernet cable between this system and the AP for damage, and replace it if necessary.</li>
            <li>Power-cycle this system and wait for it to reboot fully.</li>
            <li>If the issue persists, contact CTWI support for further assistance.</li>
          </ul>
        </li>
      </ul>
    </section>

    <div class="brand-mark"><span class="square"></span><span>CTWI</span></div>
  </main>
</div>
</body>
</html>
```